Need posters that inspire entrepreneurs

I want to create beautiful, inspiring wall art. I'm looking for a designer to create an awesome sample (note this sample is not for real use). The winning design will form the foundation of our art "style" so there will be LOTS of ongoing work for the winning designer.

It's your challenge to create a style that is clean, inspiring and timeless, and possibly can be adapted to different colour palettes.

Looking for a perfect execution of words, image and design.

The attached example shows one idea. It should serve as an idea only.

Format of the images should be either rectangular or square. Exact size is preferably UK A4 (US letter) or max A3. Assume that a display would consist of a 4 x 4 image grid so size needs to allow for that in a small to medium size office.

The quotes I want in the 3 samples (each in an individual poster - not combined in 1 poster). Each quote should have it's own, the reason for three is to prove the design work on more than one quote. The quotes are:

1) Failure is the condiment that gives success its flavor.
– Dorian Welsby

2) Whether you think you can or think you can’t, you’re right.
– Oswald Pike

3) Ever tried. Ever failed. No matter. Try Again. Fail again. Fail better.
– Lionel Marwick

Each design should include the image of the person and the quote + any design elements you consider relevant. You should find relevant images of the individuals being quoted. The final images will not be published or used commercially in any way.

Font styles to use
Serif
Sans Serif

Colors

Designer to choose colors to be used in the design.

Requirements
Must have
• Words and headshot image - 1 per poster design.
• Please consider in the design that there will not always be photographs of the person quoted and as such the design will need to hold, whether the source is a photo, sketch or something else.
Nice to have
• None, but note that the final image will be printed on a wall mounted board, printed to the edge but not on the edge. The board will have black or white edges so consider in the design.
Should not have
• None

```html
<!DOCTYPE html>
<html lang="en">
<head>
<meta charset="UTF-8">
<title>Failure is the condiment — Dorian Welsby</title>
<link href="https://fonts.googleapis.com/css2?family=Bodoni+Moda:opsz,wght@6..96,400&display=swap" rel="stylesheet">
<style>
  :root {
    --bg-black: #000000;
    --bg-green: #1c4a08;
    --portrait-light: #8a8a8a;
    --portrait-mid: #4a4a4a;
    --portrait-dark: #0a0a0a;
    --text-white: #ffffff;
  }
  html, body {
    margin: 0;
    padding: 0;
    width: 1200px;
    height: 1200px;
    overflow: hidden;
    background: var(--bg-black);
  }
  .poster {
    position: relative;
    width: 1200px;
    height: 1200px;
    background: linear-gradient(90deg, var(--bg-black) 0%, var(--bg-black) 45%, var(--bg-green) 100%);
    overflow: hidden;
  }
  .portrait {
    position: absolute;
    left: 0;
    top: 0;
    width: 310px;
    height: 1200px;
    background:
      radial-gradient(ellipse 260px 460px at 70px 470px, var(--portrait-light) 0%, var(--portrait-mid) 55%, transparent 100%),
      radial-gradient(ellipse 300px 320px at 40px 1130px, var(--portrait-mid) 0%, var(--portrait-dark) 70%, transparent 100%);
  }
  .quote {
    position: absolute;
    right: 95px;
    top: 282px;
    margin: 0;
    font-family: "Bodoni Moda", "Libre Bodoni", serif;
    font-weight: 400;
    font-size: 80px;
    line-height: 85px;
    letter-spacing: -0.5px;
    text-align: right;
    color: var(--text-white);
    text-shadow: 0 3px 10px rgba(0, 0, 0, 0.6);
  }
  .quote span { display: block; }
  .attribution {
    position: absolute;
    right: 75px;
    top: 982px;
    margin: 0;
    font-family: "Bodoni Moda", "Libre Bodoni", serif;
    font-size: 28px;
    color: var(--text-white);
    text-shadow: 0 2px 6px rgba(0, 0, 0, 0.6);
  }
</style>
</head>
<body>
  <main class="poster">
    <div class="portrait" role="img" aria-label="Black and white close-up portrait of Dorian Welsby, cropped to the left half of the face"></div>
    <blockquote class="quote">
      <span>Failure</span>
      <span>is the</span>
      <span>condiment</span>
      <span>that gives</span>
      <span>success</span>
      <span>its flavor.</span>
    </blockquote>
    <p class="attribution">Dorian Welsby</p>
  </main>
</body>
</html>
```